New world-class investment firm needs a business card design

We need a business card design for a new investment firm called 'Dalvin Soeurs & Company.' We acquire companies in the media sector and secure funding from conservative ultra, high-net worth individuals. We would like a black and white color design. We are seeking classic, elegant, and sophisticated designs. The final design should communicate financial safety, class, timelessness, and highly ethical. On the back of the business card, we would simply like the lion logo to be centered. I have attached a mock card, and variations on it are welcomed.
Industry/Entity Type
Conservative
Font styles to use
Other font styles liked:
- Garamond
Look and feel
Each slider illustrates characteristics of the customer's brand and the style your logo design should communicate.

```html
<!DOCTYPE html>
<html lang="en">
<head>
<meta charset="utf-8">
<title>Dalvin Soeurs &amp; Company — Business Card</title>
<link rel="stylesheet" href="https://fonts.googleapis.com/css2?family=EB+Garamond:wght@400;600&display=swap">
<style>
  :root {
    --backdrop: #d6d6d6;
    --card-stock: #f7f7f5;
    --ink: #111111;
    --ink-soft: #3a3a3a;
    --rule: #8a8a8a;
    --shadow: rgba(0, 0, 0, 0.28);
  }
  * { box-sizing: border-box; margin: 0; padding: 0; }
  html, body {
    width: 1200px;
    height: 800px;
    overflow: hidden;
    background: var(--backdrop);
    font-family: "EB Garamond", Garamond, Georgia, serif;
    color: var(--ink);
  }
  .card-set {
    position: relative;
    width: 1200px;
    height: 800px;
    display: flex;
    justify-content: center;
    align-items: center;
    gap: 90px;
  }
  .card {
    position: relative;
    width: 360px;
    height: 630px;
    background: var(--card-stock);
    box-shadow: 0 6px 18px var(--shadow);
  }

  /* Back side: centred mark */
  .card-back {
    display: flex;
    flex-direction: column;
    align-items: center;
    justify-content: center;
    gap: 18px;
  }
  .brand-dot {
    width: 26px;
    height: 26px;
    border-radius: 50%;
    background: var(--ink);
  }
  .brand-name {
    font-size: 24px;
    font-weight: 600;
    color: var(--ink);
    letter-spacing: 0.5px;
    text-align: center;
    line-height: 1.2;
  }

  /* Front side */
  .card-front {
    padding: 56px 44px 48px;
    display: flex;
    flex-direction: column;
  }
  .front-mark {
    display: flex;
    align-items: center;
    gap: 12px;
    margin-bottom: 60px;
  }
  .front-mark .brand-dot { width: 18px; height: 18px; }
  .front-mark .brand-name { font-size: 18px; text-align: left; }
  .company-name {
    font-size: 26px;
    font-weight: 600;
    line-height: 1.1;
  }
  .office-list {
    font-size: 15px;
    letter-spacing: 1.5px;
    color: var(--ink-soft);
    margin-top: 4px;
  }
  .office-list .divider { color: var(--rule); padding: 0 4px; }
  .person {
    margin-top: 70px;
  }
  .person-name {
    font-size: 24px;
    font-weight: 600;
    line-height: 1.1;
  }
  .person-title {
    font-size: 16px;
    color: var(--ink-soft);
    margin-top: 2px;
  }
  .contact {
    margin-top: auto;
    font-size: 17px;
    line-height: 1.8;
  }
  .contact .label { font-weight: 600; margin-right: 4px; }
</style>
</head>
<body>
  <main class="card-set">
    <section class="card card-back" aria-label="Card back">
      <span class="brand-dot" aria-hidden="true"></span>
      <span class="brand-name">Dalvin Soeurs</span>
    </section>

    <section class="card card-front" aria-label="Card front">
      <div class="front-mark">
        <span class="brand-dot" aria-hidden="true"></span>
        <span class="brand-name">Dalvin Soeurs</span>
      </div>
      <h1 class="company-name">Dalvin Soeurs &amp; Company</h1>
      <p class="office-list">New York<span class="divider">|</span>Los Angeles<span class="divider">|</span>Geneva</p>

      <div class="person">
        <h2 class="person-name">Julien A. Dalvin</h2>
        <p class="person-title">Chairman &amp; CEO</p>
      </div>

      <div class="contact">
        <p><span class="label">P:</span>212.555.0148</p>
        <p><span class="label">E:</span>julien@dalvinsoeurs.com</p>
      </div>
    </section>
  </main>
</body>
</html>
```